Insurance Company Website Design

We are working with an insurance company. They sell home, auto, commercial, and health insurance. We like the "get a quote" in the banner of https://www.plovanta.example and https://www.quirelmog.example.

Some sites to use for content/competitors and inspiration:
https://velturbrookins.example
https://kamzubredainsurance.example
https://tvorpinsurance.example
https://www.insuranceforzelmarids.example
https://www.plovanta.example
https://www.quirelmog.example

Thank you for taking the time to consider designing a website for us. We are web developers based in Stockton, CA, USA. Most of our projects go through the same process. Understanding this process may help you win a project with us. We custom-code all of our websites in-house. We don’t have any requirements as to what tools you use for your design, but we ask that you follow these guidelines.

IMAGES:
If you use any images or icons in the design, we ask that you have a link to the asset so we can purchase the image/icon. Most of the designs we submit do not have the customer’s images on them unless they have some great images. Be creative; show us the feeling you are trying to portray with your image choices. Use any royalty-free site you choose. We subscribe to Quintrel and mainly use their images, but we can purchase images outside of Quintrel. PLEASE NOTE: we will not submit designs to clients with watermarks on the images.

FONTS:
We ask that you identify the fonts you’re using in the design. This can be done in a message if you want. We typically use Google Fonts and Quintrel Fonts.

CONTENT:
We're always open to different content and ideas. We often submit designs with stock images so the client can see our vision. We typically take pictures after the website launch to use their images with our vision. Lorem Ipsum is fine for paragraphs, but we ask that you make the Headers with correct English. We want to be able to show the vision and identify the sections of the website.

INSPIRATION:
We typically add a couple of links in the brief of websites we like to help you get started in your design.

REVISIONS:
We do not often ask for revisions of the designs unless we see something in the design that may not appeal to the client. If there are slight changes that we want to make, we do that in the development process.

FEEDBACK:
We rarely give feedback on designs during the design process. We are working on many website projects and do not have the time to provide feedback. We usually respond if your request is well thought out and asks specific questions, but a note asking “feedback, please” usually goes unanswered.

```html
<!DOCTYPE html>
<html lang="en">
<head>
<meta charset="utf-8">
<title>Covella Insurance</title>
<link href="https://fonts.googleapis.com/css2?family=Poppins:wght@400;500;600;700&display=swap" rel="stylesheet">
<style>
:root{
  --blue:#0b5cad;
  --sky:#58bdf0;
  --pale:#eef7fd;
  --ink:#333333;
  --text:#555555;
  --card:#f3f3f3;
  --footer:#333333;
  --white:#ffffff;
}
*{box-sizing:border-box;margin:0;padding:0}
html,body{width:1200px;height:4152px;overflow:hidden}
body{font-family:'Poppins',sans-serif;color:var(--ink);background:var(--white);position:relative}
.wrap{width:1052px;margin:0 auto;position:relative;height:100%}
.eyebrow{font-size:20px;font-weight:400;color:var(--blue);text-align:center;letter-spacing:.5px}
.title{font-size:36px;font-weight:700;color:var(--ink);text-align:center;letter-spacing:.5px;margin-top:2px}
.arrow{position:absolute;top:50%;width:22px;height:34px;transform:translateY(-50%)}
.arrow.left{left:-40px}.arrow.right{right:-40px}
.btn-outline{display:block;width:178px;height:52px;margin:0 auto;border:2px solid var(--sky);border-radius:26px;text-align:center;line-height:48px;font-weight:600;font-size:16px;color:var(--sky);letter-spacing:.5px}

/* header */
.site-header{height:81px;background:var(--white);position:relative}
.brand{position:absolute;left:74px;top:14px;display:flex;align-items:center;gap:10px}
.brand-dot{width:14px;height:14px;border-radius:50%;background:var(--sky)}
.brand-name{font-size:34px;font-weight:500;color:var(--blue);letter-spacing:.5px}
.main-nav{position:absolute;left:355px;top:30px;display:flex}
.main-nav a{font-size:15px;font-weight:600;color:var(--ink);text-decoration:none;margin-right:41px}
.main-nav a.active{color:var(--blue)}
.header-cta{position:absolute;left:958px;top:19px;width:168px;height:46px;border-radius:23px;background:var(--sky);color:var(--white);font-weight:600;font-size:17px;text-align:center;line-height:46px}

/* hero */
.hero{height:574px;background:linear-gradient(90deg,#c4e5f9 0%,#d8eefb 55%,#bfe2f8 100%);position:relative;overflow:hidden}
.quote-card{position:absolute;left:74px;top:92px;width:421px;height:392px;background:rgba(255,255,255,.45);border-radius:20px;padding:38px 24px}
.quote-card h1{font-size:31px;font-weight:700;color:var(--ink);letter-spacing:1px}
.quote-card h2{font-size:24px;font-weight:600;color:var(--blue);line-height:1.3;margin-top:6px}
.field{height:51px;border:1.5px solid #a8b8c8;background:var(--white);border-radius:26px;padding:0 24px;line-height:48px;font-size:14px;color:var(--ink);position:relative}
.field.first{margin-top:28px}
.field+.field{margin-top:12px}
.field .caret{position:absolute;right:22px;top:18px}
.quote-submit{margin-top:12px;height:52px;border-radius:26px;background:var(--blue);color:var(--white);font-weight:700;font-size:18px;text-align:center;line-height:52px;letter-spacing:.5px}
.hero-photo{position:absolute;left:694px;top:10px;width:371px;height:564px;border-radius:180px 180px 0 0;background:linear-gradient(180deg,#5b6f88 0%,#1d2c45 55%,#17233a 100%)}

/* services */
.services{height:516px;padding-top:62px}
.service-row{display:flex;gap:28px;margin-top:34px;position:relative}
.service-card{width:242px;height:284px;border-radius:6px;color:var(--white);text-align:center;padding-top:26px}
.service-card.light{background:var(--sky)}
.service-card.dark{background:var(--blue)}
.service-card svg{width:96px;height:80px}
.service-card h3{font-size:21px;font-weight:600;line-height:1.35;margin-top:8px}
.service-card p{font-size:13px;line-height:1.65;margin-top:8px;padding:0 10px;opacity:.9}

/* about */
.about{height:503px;background:linear-gradient(90deg,#0d5bb0 0%,#1d78cc 55%,#4eb6ec 100%);color:var(--white)}
.about-text{position:absolute;left:0;top:82px;width:570px}
.about-text .tag{font-size:20px}
.about-text h2{font-size:36px;font-weight:700;margin-top:2px;letter-spacing:.5px}
.about-text p{font-size:14.5px;line-height:2;margin-top:14px}
.about-btn{margin-top:34px;width:178px;height:52px;border:2px solid var(--white);border-radius:26px;text-align:center;line-height:48px;font-weight:600;font-size:16px}
.about-photo{position:absolute;left:595px;top:55px;width:457px;height:395px;border-radius:58% 42% 46% 54% / 46% 58% 42% 54%;background:linear-gradient(135deg,#3a3a3a 0%,#8d8d8d 50%,#f2f2f2 100%)}

/* faq */
.faq{height:587px;padding-top:52px}
.faq-row{display:flex;gap:34px;margin-top:40px;position:relative}
.faq-card{width:328px;height:269px;background:var(--card);border-radius:6px;padding:28px 21px}
.faq-card h3{font-size:21px;font-weight:600;color:var(--blue);line-height:1.4}
.faq-card p{font-size:13.5px;line-height:1.78;color:var(--text);margin-top:12px}
.faq .btn-outline{margin-top:47px}

/* testimonials */
.testimonials{height:410px;background:var(--pale);padding-top:66px}
.testimonial-row{display:flex;gap:56px;margin-top:40px;position:relative}
.testimonial{width:314px}
.t-head{display:flex;gap:16px;align-items:flex-start}
.q-badge{width:48px;height:48px;border-radius:50%;background:var(--blue);color:var(--white);font-size:30px;font-weight:700;text-align:center;line-height:56px}
.t-head h4{font-size:19px;font-weight:500;margin-top:2px}
.stars{color:#f5a623;font-size:18px;letter-spacing:5px;line-height:1.2}
.testimonial p{font-size:13.5px;line-height:1.8;color:var(--text);margin-top:12px;white-space:nowrap}

/* appointment */
.appointment{height:494px;background:var(--blue)}
.appt-photo{position:absolute;left:0;top:52px;width:458px;height:388px;border-radius:48% 52% 60% 40% / 40% 46% 54% 60%;background:linear-gradient(150deg,#dfe6ee 0%,#9aa9bb 55%,#46566d 100%)}
.appt-form{position:absolute;left:542px;top:48px;width:510px;color:var(--white)}
.appt-form .tag{font-size:20px}
.appt-form h2{font-size:36px;font-weight:700;letter-spacing:.5px}
.form-grid{display:grid;grid-template-columns:248px 248px;gap:16px 14px;margin-top:16px}
.in{height:46px;border:1.5px solid var(--sky);border-radius:23px;padding:0 22px;line-height:43px;font-size:13.5px}
.in.msg{grid-column:1/3;height:108px;border-radius:20px;line-height:1;padding-top:16px}
.appt-submit{margin-top:12px;width:248px;height:43px;border-radius:22px;background:var(--sky);text-align:center;line-height:43px;font-weight:600;font-size:16px}

/* news */
.news{height:658px;padding-top:58px}
.news-row{display:flex;gap:34px;margin-top:42px}
.news-card{width:328px}
.news-img{height:196px;border-radius:6px}
.news-img.a{background:linear-gradient(135deg,#e9e4df,#b99c85 60%,#6f5a4a)}
.news-img.b{background:linear-gradient(135deg,#d9e8f5,#6d9ccc 55%,#2f5f9a)}
.news-img.c{background:linear-gradient(135deg,#9fb4c6,#5a6b7c 50%,#2f3c4a)}
.news-card .date{font-size:13.5px;font-weight:600;color:var(--blue);margin-top:24px}
.news-card h3{font-size:21px;font-weight:500;line-height:1.4;margin-top:4px}
.news-card .more{font-size:13.5px;font-weight:500;color:var(--sky);margin-top:10px}
.news .btn-outline{margin-top:60px}

/* footer */
.site-footer{height:329px;background:var(--footer);color:var(--white)}
.f-brand{position:absolute;left:0;top:78px}
.f-brand .name{font-size:46px;font-weight:400;letter-spacing:.5px}
.f-brand small{display:block;font-size:12px;color:#c8c8c8;line-height:1.5;margin-top:8px}
.socials{display:flex;gap:14px;margin-top:16px}
.socials span{width:22px;height:22px;border-radius:50%;background:var(--sky)}
.f-col{position:absolute;top:58px}
.f-col h4{font-size:18px;font-weight:600;color:var(--sky);margin-bottom:8px}
.f-col li{list-style:none;font-size:14.5px;line-height:31px}
.f-col.f-services li{line-height:35px}
.f-contact li{display:flex;gap:14px;align-items:flex-start;line-height:27px;margin-bottom:8px}
.f-contact svg{width:16px;height:16px;margin-top:5px;flex:none}
</style>
</head>
<body>

<header class="site-header">
  <div class="brand"><span class="brand-dot"></span><span class="brand-name">covella</span></div>
  <nav class="main-nav">
    <a class="active">Home</a><a>About Us</a><a>Services</a><a>Our Team</a><a>Blog</a><a>Contact Us</a>
  </nav>
  <div class="header-cta">Get a Quote</div>
</header>

<section class="hero">
  <div class="quote-card">
    <h1>REQUEST A QUOTE</h1>
    <h2>Create an affordable price,<br>just for you.</h2>
    <div class="field first">Select Product
      <svg class="caret" width="10" height="14" viewBox="0 0 10 14"><path d="M1 6 5 1 9 6Z M1 8 5 13 9 8Z" fill="#333"/></svg>
    </div>
    <div class="field">Enter ZIP Code</div>
    <div class="quote-submit">GET A QUOTE</div>
  </div>
  <div class="hero-photo" role="img" aria-label="Smiling insurance agent in a dark suit holding a folder"></div>
</section>

<section class="services">
  <div class="wrap">
    <p class="eyebrow">WHAT WE DO</p>
    <h2 class="title">OUR INSURANCE SERVICES</h2>
    <div class="service-row">
      <svg class="arrow left" viewBox="0 0 22 34"><path d="M18 3 4 17 18 31" fill="none" stroke="#333" stroke-width="2.5"/></svg>
      <div class="service-card light">
        <svg viewBox="0 0 96 80" fill="none" stroke="#fff" stroke-width="2.5"><path d="M8 38 40 12 72 38M16 32v40h48V32M32 72V50h16v22"/><path d="M66 40l12 5v10c0 8-6 13-12 15-6-2-12-7-12-15V45z"/><path d="M61 55l4 4 7-8"/></svg>
        <h3>Home<br>Insurance</h3>
        <p>Sed ut perspiciatis<br>unde omnis iste natus error sit<br>voluptatem accusantium<br>doloremquelauda.</p>
      </div>
      <div class="service-card dark">
        <svg viewBox="0 0 96 80" fill="none" stroke="#fff" stroke-width="2.5"><path d="M10 50V38l8-16h36l8 16v12H10z"/><circle cx="22" cy="54" r="6"/><circle cx="50" cy="54" r="6"/><path d="M18 36h40"/><path d="M70 22l14 6v12c0 10-7 16-14 18-7-2-14-8-14-18V28z"/><path d="M64 40l5 5 9-10"/></svg>
        <h3>Auto<br>Insurance</h3>
        <p>Sed ut perspiciatis<br>unde omnis iste natus error sit<br>voluptatem accusantium<br>doloremquelauda.</p>
      </div>
      <div class="service-card light">
        <svg viewBox="0 0 96 80" fill="none" stroke="#fff" stroke-width="2.5"><path d="M20 74V18h30v56M50 32h20v42M14 74h64"/><path d="M27 26h6M38 26h6M27 36h6M38 36h6M27 46h6M38 46h6M27 56h6M38 56h6M56 42h8M56 52h8M56 62h8"/><path d="M72 8l10 4v8c0 7-5 11-10 13-5-2-10-6-10-13v-8z"/></svg>
        <h3>Commercial<br>Insurance</h3>
        <p>Sed ut perspiciatis<br>unde omnis iste natus error sit<br>voluptatem accusantium<br>doloremquelauda.</p>
      </div>
      <div class="service-card dark">
        <svg viewBox="0 0 96 80" fill="none" stroke="#fff" stroke-width="2.5"><path d="M18 6h36l10 10v56H18z"/><path d="M36 18v14M29 25h14M26 42h28M26 50h20M26 58h16"/><path d="M70 40l14 6v12c0 10-7 16-14 18-7-2-14-8-14-18V46z"/><path d="M64 58l5 5 9-10"/></svg>
        <h3>Health<br>Insurance</h3>
        <p>Sed ut perspiciatis<br>unde omnis iste natus error sit<br>voluptatem accusantium<br>doloremquelauda.</p>
      </div>
      <svg class="arrow right" viewBox="0 0 22 34"><path d="M4 3 18 17 4 31" fill="none" stroke="#333" stroke-width="2.5"/></svg>
    </div>
  </div>
</section>

<section class="about">
  <div class="wrap">
    <div class="about-text">
      <p class="tag">WHO WE ARE</p>
      <h2>ABOUT COVELLA INSURANCE</h2>
      <p>Sed ut perspiciatis unde omnis iste natus error sit voluptatem<br>accusantium doloremque laudantium, totam rem aperiam, eaque ipsa<br>quae ab illo inventore veritatis et quasi architecto beatae vitae dicta sunt<br>explicabo. Nemo enim ipsam voluptatem quia voluptas sit aspernatur aut<br>odit aut fugit, sed quia consequuntur magni dolores eos qui ratione<br>voluptatem sequi nesciunt.</p>
      <div class="about-btn">READ MORE</div>
    </div>
    <div class="about-photo" role="img" aria-label="Hand holding an umbrella over paper cut-outs of a family, car and house"></div>
  </div>
</section>

<section class="faq">
  <div class="wrap">
    <p class="eyebrow">QUESTION &amp; ANSWER</p>
    <h2 class="title">FREQUENTLY ASKED QUESTIONS</h2>
    <div class="faq-row">
      <svg class="arrow left" viewBox="0 0 22 34"><path d="M18 3 4 17 18 31" fill="none" stroke="#333" stroke-width="2.5"/></svg>
      <div class="faq-card"><h3>Sed ut perspiciatis unde omnis iste natus?</h3><p>Nemo enim ipsam voluptatem quia voluptas sit aspernatur aut odit aut fugit, sed quia consequuntur magni dolores eos qui ratione voluptatem sequi nesciunt incidunt ut labore et dolore magnam aliquam quaerat voluptatem.</p></div>
      <div class="faq-card"><h3>Sed ut perspiciatis unde omnis iste natus?</h3><p>Nemo enim ipsam voluptatem quia voluptas sit aspernatur aut odit aut fugit, sed quia consequuntur magni dolores eos qui ratione voluptatem sequi nesciunt incidunt ut labore et dolore magnam aliquam quaerat voluptatem.</p></div>
      <div class="faq-card"><h3>Sed ut perspiciatis unde omnis iste natus?</h3><p>Nemo enim ipsam voluptatem quia voluptas sit aspernatur aut odit aut fugit, sed quia consequuntur magni dolores eos qui ratione voluptatem sequi nesciunt incidunt ut labore et dolore magnam aliquam quaerat voluptatem.</p></div>
      <svg class="arrow right" viewBox="0 0 22 34"><path d="M4 3 18 17 4 31" fill="none" stroke="#333" stroke-width="2.5"/></svg>
    </div>
    <div class="btn-outline">VIEW ALL FAQ'S</div>
  </div>
</section>

<section class="testimonials">
  <div class="wrap">
    <p class="eyebrow">TESTIMONIALS</p>
    <h2 class="title">WHAT PEOPLE ARE SAYING</h2>
    <div class="testimonial-row">
      <svg class="arrow left" viewBox="0 0 22 34"><path d="M18 3 4 17 18 31" fill="none" stroke="#333" stroke-width="2.5"/></svg>
      <div class="testimonial">
        <div class="t-head"><div class="q-badge">“</div><div><h4>Name Heading</h4><div class="stars">★★★★★</div></div></div>
        <p>“ Sed ut perspiciatis unde omnis iste natus<br>error sit voluptatem accusantium doloremque<br>laudantium quasi architecto beatae<br>vitae dicta sunt..”</p>
      </div>
      <div class="testimonial">
        <div class="t-head"><div class="q-badge">“</div><div><h4>Name Heading</h4><div class="stars">★★★★★</div></div></div>
        <p>“ Sed ut perspiciatis unde omnis iste natus<br>error sit voluptatem accusantium doloremque<br>laudantium quasi architecto beatae<br>vitae dicta sunt..”</p>
      </div>
      <div class="testimonial">
        <div class="t-head"><div class="q-badge">“</div><div><h4>Name Heading</h4><div class="stars">★★★★★</div></div></div>
        <p>“ Sed ut perspiciatis unde omnis iste natus<br>error sit voluptatem accusantium doloremque<br>laudantium quasi architecto beatae<br>vitae dicta sunt..”</p>
      </div>
      <svg class="arrow right" viewBox="0 0 22 34"><path d="M4 3 18 17 4 31" fill="none" stroke="#333" stroke-width="2.5"/></svg>
    </div>
  </div>
</section>

<section class="appointment">
  <div class="wrap">
    <div class="appt-photo" role="img" aria-label="Smiling advisor in a grey blazer holding a tablet"></div>
    <div class="appt-form">
      <p class="tag">GET IN TOUCH</p>
      <h2>BOOK AN APPOINTMENT</h2>
      <div class="form-grid">
        <div class="in">Name</div><div class="in">Email Address</div>
        <div class="in">Phone No</div><div class="in">Subject</div>
        <div class="in msg">Message</div>
      </div>
      <div class="appt-submit">SUBMIT NOW</div>
    </div>
  </div>
</section>

<section class="news">
  <div class="wrap">
    <p class="eyebrow">WHAT'S NEW?</p>
    <h2 class="title">LATEST NEWS UPDATE</h2>
    <div class="news-row">
      <article class="news-card">
        <div class="news-img a" role="img" aria-label="Hands sheltering a small model house"></div>
        <p class="date">Jan 25, 2024</p>
        <h3>Sed ut perspiciatis unde omnis iste natus&nbsp; error sit..</h3>
        <p class="more">Read More</p>
      </article>
      <article class="news-card">
        <div class="news-img b" role="img" aria-label="Stethoscope resting on a health insurance card"></div>
        <p class="date">Jan 25, 2024</p>
        <h3>Sed ut perspiciatis unde omnis iste natus&nbsp; error sit..</h3>
        <p class="more">Read More</p>
      </article>
      <article class="news-card">
        <div class="news-img c" role="img" aria-label="Advisor meeting with a client at a desk"></div>
        <p class="date">Jan 25, 2024</p>
        <h3>Sed ut perspiciatis unde omnis iste natus&nbsp; error sit..</h3>
        <p class="more">Read More</p>
      </article>
    </div>
    <div class="btn-outline">VIEW ALL NEWS</div>
  </div>
</section>

<footer class="site-footer">
  <div class="wrap">
    <div class="f-brand">
      <div class="name">covella</div>
      <small>Copyright © 2024.Company Name<br>All Right Reserved</small>
      <div class="socials"><span></span><span></span><span></span><span></span><span></span></div>
    </div>
    <div class="f-col" style="left:282px">
      <h4>Quick Links</h4>
      <ul><li>Home</li><li>About Us</li><li>Services</li><li>Our Team</li><li>Blog</li><li>Contact Us</li></ul>
    </div>
    <div class="f-col f-services" style="left:532px">
      <h4>Services</h4>
      <ul><li>Home Insurance</li><li>Auto Insurance</li><li>Commercial Insurance</li><li>Health Insurance</li></ul>
    </div>
    <div class="f-col f-contact" style="left:810px">
      <h4>Contact Address</h4>
      <ul>
        <li><svg viewBox="0 0 16 16"><path d="M8 1a5 5 0 0 0-5 5c0 4 5 9 5 9s5-5 5-9a5 5 0 0 0-5-5zm0 7a2 2 0 1 1 0-4 2 2 0 0 1 0 4z" fill="#58bdf0"/></svg><span>48 Harrow Lane Suite 210,<br>Brenmoor 20417, United State</span></li>
        <li><svg viewBox="0 0 16 16"><path d="M4 1h3l1 4-2 1.5a9 9 0 0 0 3.5 3.5L11 8l4 1v3a2 2 0 0 1-2 2A12 12 0 0 1 2 3a2 2 0 0 1 2-2z" fill="#58bdf0"/></svg><span>+100-555-0142</span></li>
        <li><svg viewBox="0 0 16 16"><path d="M1 3h14v10H1zM1 3l7 6 7-6" fill="#58bdf0" stroke="#333" stroke-width="1.2"/></svg><span>hello@covella.example</span></li>
      </ul>
    </div>
  </div>
</footer>

</body>
</html>
```